Info graphic to explain a fee hierarchy

We need a clean and current feeling graphical representation of what a typical fee structure looks like from our competitors, with an accompanying one highlighting the simplicity and transparency of ours.

We will be using this online on our web page and in blog posts. Solutions that can be animated would be looked upon favourably.
however, ideally would like to avoid any Flash based solutions.

I have provided the fee structure comparison and some notes for each component of a typical fee in both excel and a jpg of the excel file. Not fussed with the graph design however a 'stacked' fee graph could get the point across nicely. Up to you.

I have provided a low and high estimate for our competitors. You don't have to include the figures however the proportions in the graph could be a way around cluttering the design with numbers.

I have also included our logo to give you an idea of colours.

Target Market(s)

Gen X and Gen y, internet savvy, financially competent

Industry/Entity Type

Financial Service

Font styles to use
Sans Serif

Requirements
Must have
• Graphical based solution - easy to read and understand
Nice to have
• Potential to be animated, PSD (or similar) with layering so that it is easy to implement for use with HTML 5 or JQuery web pages
Should not have
• Flash solutions

```html
<!DOCTYPE html>
<html lang="en">
<head>
<meta charset="utf-8">
<title>Fee Structure</title>
<link href="https://fonts.googleapis.com/css2?family=Lato:wght@400;700&display=swap" rel="stylesheet">
<style>
  :root{
    --page:#2c2c2c;
    --paper:#ffffff;
    --orange:#ec8b46;
    --blue-ink:#2f4f96;
    --navy:#1f3a78;
    --yellow-ink:#e0a60c;
    --green-ink:#3f7a25;
    --orange-ink:#e0742a;
    --text:#333333;
    --muted:#6b6b6b;
    --ring:#c9c9c9;
  }
  html,body{margin:0;padding:0;width:1200px;height:1200px;overflow:hidden;background:var(--page);}
  body{font-family:'Lato',sans-serif;position:relative;}
  .frame{position:absolute;left:0;top:212px;width:1200px;height:776px;overflow:hidden;}
  .infographic{position:absolute;left:0;top:0;width:1340px;height:867px;background:var(--paper);transform:scale(0.89552);transform-origin:0 0;}
  .graphics{position:absolute;left:0;top:0;width:1340px;height:867px;}
  .title-band{position:absolute;left:348px;top:0;width:644px;height:108px;background:var(--orange);display:flex;align-items:center;justify-content:center;}
  .title-band h1{margin:0;color:#fff;font-weight:700;font-size:66px;letter-spacing:7px;}
  .fee{position:absolute;}
  .fee-name{margin:0;font-weight:400;font-size:20px;line-height:23px;}
  .fee-desc{margin:2px 0 0;font-size:14px;line-height:17px;color:var(--muted);}
  .range{position:absolute;font-size:11px;line-height:13px;color:var(--text);text-transform:uppercase;}
  .range b{display:block;font-size:16px;line-height:18px;font-weight:700;margin-bottom:6px;text-transform:none;}
  .is-blue{color:var(--blue-ink);}
  .is-dark{color:var(--text);}
  .is-yellow{color:var(--yellow-ink);}
  .is-green{color:var(--green-ink);}
  .is-orange{color:var(--orange-ink);}
  .centered{text-align:center;}
  .brand{position:absolute;left:938px;top:210px;width:200px;display:flex;align-items:center;gap:10px;}
  .brand-mark{width:14px;height:14px;border-radius:50%;background:var(--navy);}
  .brand-name{font-size:26px;font-weight:700;color:var(--navy);}
  .own-value{position:absolute;font-size:17px;font-weight:700;}
</style>
</head>
<body>
<div class="frame">
<div class="infographic">

  <svg class="graphics" viewBox="0 0 1340 867" aria-hidden="true">
    <g fill="none" stroke-width="1" stroke-dasharray="4 3">
      <polyline points="195,156 273,156 273,260 322,260" stroke="#7d8fb8"/>
      <polyline points="193,314 268,314 268,380 322,380" stroke="#b5b5b5"/>
      <polyline points="283,474 293,474 293,447 322,447" stroke="#e6b93a"/>
      <polyline points="216,688 296,688 296,512 322,512" stroke="#7da860"/>
      <polyline points="583,176 558,176 558,322 531,322" stroke="#e9935a"/>
      <polyline points="681,384 560,384 560,568 531,568" stroke="#e9935a"/>
      <polyline points="802,384 880,384 880,447 916,447" stroke="#e9935a"/>
      <polyline points="686,572 574,572 574,634 531,634" stroke="#6d8cc8"/>
      <polyline points="796,572 880,572 880,510 916,510" stroke="#6d8cc8"/>
      <polyline points="1123,439 1163,439" stroke="#e9935a"/>
      <polyline points="1123,518 1163,518" stroke="#6d8cc8"/>
    </g>

    <!-- competitor stack, bottom layer first -->
    <g class="stack">
      <g><polygon points="323,619 427,619 427,707 323,647" fill="#3a62a4"/><polygon points="427,619 531,619 531,647 427,707" fill="#4c75c0"/><polygon points="427,559 531,619 427,679 323,619" fill="#6d95d0"/></g>
      <g><polygon points="323,556 427,556 427,644 323,584" fill="#cc6a31"/><polygon points="427,556 531,556 531,584 427,644" fill="#e07b35"/><polygon points="427,496 531,556 427,616 323,556" fill="#ec8d4f"/></g>
      <g><polygon points="323,496 427,496 427,584 323,524" fill="#17293b"/><polygon points="427,496 531,496 531,524 427,584" fill="#2a3f55"/><polygon points="427,436 531,496 427,556 323,496" fill="#4a6278"/></g>
      <g><polygon points="323,432 427,432 427,520 323,460" fill="#e2b02a"/><polygon points="427,432 531,432 531,460 427,520" fill="#f8c810"/><polygon points="427,372 531,432 427,492 323,432" fill="#fdd540"/></g>
      <g><polygon points="323,342 427,342 427,430 323,370" fill="#bdbdbd"/><polygon points="427,342 531,342 531,370 427,430" fill="#a8a8a8"/><polygon points="427,282 531,342 427,402 323,342" fill="#484848"/></g>
      <g><polygon points="323,310 427,310 427,398 323,338" fill="#cc6a31"/><polygon points="427,310 531,310 531,338 427,398" fill="#e07b35"/><polygon points="427,250 531,310 427,370 323,310" fill="#ec8d4f"/></g>
      <g><polygon points="323,249 427,249 427,337 323,277" fill="#3a62a4"/><polygon points="427,249 531,249 531,277 427,337" fill="#4c75c0"/><polygon points="427,189 531,249 427,309 323,249" fill="#6d95d0"/></g>
    </g>

    <!-- own stack -->
    <g class="stack stack--own">
      <g><polygon points="916,494 1019,494 1019,582 916,522" fill="#3a62a4"/><polygon points="1019,494 1122,494 1122,522 1019,582" fill="#4c75c0"/><polygon points="1019,434 1122,494 1019,554 916,494" fill="#6d95d0"/></g>
      <g><polygon points="916,435 1019,435 1019,523 916,463" fill="#cc6a31"/><polygon points="1019,435 1122,435 1122,463 1019,523" fill="#e07b35"/><polygon points="1019,375 1122,435 1019,495 916,435" fill="#ec8d4f"/></g>
    </g>

    <!-- rings: grey track with coloured share -->
    <g fill="none" stroke-width="2.5">
      <g transform="translate(118,242) rotate(-90)"><circle r="28" stroke="var(--ring)"/><circle r="28" stroke="#5f84c6" stroke-dasharray="140 176"/></g>
      <g transform="translate(119,398) rotate(-90)"><circle r="28" stroke="var(--ring)"/><circle r="28" stroke="#4a4a4a" stroke-dasharray="14 176"/></g>
      <g transform="translate(118,600) rotate(-90)"><circle r="28" stroke="var(--ring)"/><circle r="28" stroke="#e6b320" stroke-dasharray="14 176"/></g>
      <g transform="translate(118,777) rotate(-90)"><circle r="28" stroke="var(--ring)"/><circle r="28" stroke="#3f7a25" stroke-dasharray="9 176"/></g>
      <g transform="translate(617,270) rotate(-90)"><circle r="28" stroke="var(--ring)"/><circle r="28" stroke="#a94d1e" stroke-dasharray="53 176"/></g>
      <g transform="translate(706,457) rotate(-90)"><circle r="28" stroke="var(--ring)"/><circle r="28" stroke="#b85a22" stroke-dasharray="80 176"/></g>
      <g transform="translate(706,670) rotate(-90)"><circle r="28" stroke="#2f4f96"/></g>
      <g transform="translate(1194,434) rotate(-90)"><circle r="28" stroke="var(--ring)"/><circle r="28" stroke="#ec8b46" stroke-dasharray="80 176"/></g>
      <g transform="translate(1194,520) rotate(-90)"><circle r="28" stroke="var(--ring)"/><circle r="28" stroke="#2f4f96" stroke-dasharray="150 176"/></g>
    </g>
  </svg>

  <header class="title-band"><h1>FEE STRUCTURE</h1></header>

  <section class="fee" style="left:88px;top:142px;width:200px;">
    <h2 class="fee-name is-blue">Adviser Fee</h2>
    <p class="fee-desc">Adviser cost for ongoing<br>service arrangement</p>
  </section>
  <div class="range" style="left:164px;top:209px;">Low end<b class="is-blue">0.40%</b>High end<b class="is-blue">1.00%</b></div>

  <section class="fee" style="left:88px;top:300px;width:200px;">
    <h2 class="fee-name is-dark">Trustee Fee</h2>
    <p class="fee-desc" style="padding-left:4px;">Superannuation<br>Trustee Fee</p>
  </section>
  <div class="range" style="left:165px;top:365px;">Low end<b class="is-dark">0.10%</b>High end<b class="is-dark">0.20%</b></div>

  <section class="fee" style="left:88px;top:462px;width:200px;">
    <h2 class="fee-name is-yellow">Investment Board Fee</h2>
    <p class="fee-desc">Cost of selecting the various<br>money managers - i.e. which<br>equities manager or which<br>bond manager</p>
  </section>
  <div class="range" style="left:164px;top:566px;">Low end<b class="is-yellow">0.10%</b>High end<b class="is-yellow">0.20%</b></div>

  <section class="fee" style="left:88px;top:651px;width:260px;">
    <h2 class="fee-name is-green">Asset<br>Allocation fee</h2>
    <p class="fee-desc">Cost of choosing between Equities,<br>bonds, cash - not all funds have this cost</p>
  </section>
  <div class="range" style="left:164px;top:743px;">Low end<b class="is-green">0.05%</b>High end<b class="is-green">0.15%</b></div>

  <section class="fee" style="left:588px;top:161px;width:220px;">
    <h2 class="fee-name is-orange">Dealer Group</h2>
    <p class="fee-desc">Cost of Aust. Fin. Service<br>Licensing &amp; product selection</p>
  </section>
  <div class="range" style="left:662px;top:236px;">Low end<b class="is-blue">0.10%</b>High end<b class="is-blue">0.30%</b></div>

  <section class="fee centered" style="left:592px;top:370px;width:300px;">
    <h2 class="fee-name is-orange">Platform Fee</h2>
    <p class="fee-desc" style="margin-top:-1px;">Cost of providing the investment platform</p>
  </section>
  <div class="range" style="left:751px;top:422px;">Low end<b class="is-yellow">0.20%</b>High end<b class="is-yellow">0.50%</b></div>

  <section class="fee centered" style="left:592px;top:559px;width:300px;">
    <h2 class="fee-name is-blue">Investment<br>Management Fee</h2>
    <p class="fee-desc">Actual Fee going to the investment managers</p>
  </section>
  <div class="range" style="left:751px;top:636px;">Low end<b class="is-blue">0.40%</b>High end<b class="is-blue">1.20%</b></div>

  <div class="brand">
    <span class="brand-mark"></span>
    <span class="brand-name">Keystone Wealth</span>
  </div>

  <div class="own-value is-orange" style="left:1236px;top:421px;">0.40%</div>
  <div class="own-value is-blue" style="left:1236px;top:506px;">0.60%</div>

</div>
</div>
</body>
</html>
```